Quill Brook Syrup labels

Design for 3" round labels for 8 oz. maple syrup jars. Must include a picture (or outline) of an irish setter, a maple leaf (?) and the name "Quill Brook Syrup" and the location Bramble Lake, Vermont. 8 fl oz (237 ml) and Grade A Amber. Here's my shitty stab at it. I want less leaf and more dog. I've included marginal pictures of the dog. I would prefer the dog center in the middle and the leaf behind it.

```html
<!DOCTYPE html>
<html lang="en">
<head>
<meta charset="utf-8">
<title>Quill Brook Syrup – Maple Syrup Label</title>
<link href="https://fonts.googleapis.com/css2?family=Noto+Serif:wght@400;600;700;900&display=swap" rel="stylesheet">
<style>
  :root {
    --cream: #fde6cc;
    --label-red: #f2403c;
    --ink: #111111;
    --ink-soft: #3a2f2a;
    --page: #ffffff;
    --dog-dark: #4a2418;
    --dog-mid: #7a3322;
    --leaf-red: #d8261e;
  }
  html, body {
    margin: 0;
    padding: 0;
    width: 991px;
    height: 1200px;
    overflow: hidden;
    background: var(--page);
  }
  .canvas {
    position: relative;
    width: 991px;
    height: 1200px;
  }
  .label {
    position: absolute;
    left: 55px;
    top: 160px;
    width: 880px;
    height: 880px;
    font-family: "Noto Serif", Georgia, serif;
  }
  .arc-title { font-size: 29px; font-weight: 600; fill: var(--ink-soft); letter-spacing: 1px; }
  .arc-place { font-size: 27px; font-weight: 600; fill: var(--ink-soft); letter-spacing: 1px; }
  .grade { font-size: 11px; font-weight: 600; fill: var(--ink-soft); }
  .product-main { font-size: 100px; font-weight: 900; fill: var(--ink); letter-spacing: -2px; }
  .product-sub { font-size: 58px; font-weight: 700; fill: var(--ink); letter-spacing: 4px; }
  .volume { font-size: 18px; font-weight: 600; fill: var(--ink-soft); }
</style>
</head>
<body>
<main class="canvas">
  <svg class="label" viewBox="-275 -275 550 550" xmlns="http://www.w3.org/2000/svg">
    <defs>
      <path id="arc-top" d="M -205 0 A 205 205 0 0 1 205 0"/>
      <path id="arc-bottom" d="M -230 0 A 230 230 0 0 0 230 0"/>
      <radialGradient id="dog-fill" cx="45%" cy="45%" r="60%">
        <stop offset="0%" stop-color="var(--dog-mid)"/>
        <stop offset="60%" stop-color="var(--dog-dark)"/>
        <stop offset="100%" stop-color="var(--leaf-red)"/>
      </radialGradient>
    </defs>

    <circle class="label-base" r="275" fill="var(--cream)"/>
    <circle class="label-band" r="255" fill="none" stroke="var(--label-red)" stroke-width="22"/>

    <circle class="frame-ring" r="195" fill="none" stroke="var(--label-red)" stroke-width="2"/>
    <line class="frame-rule" x1="-184" y1="-65" x2="184" y2="-65" stroke="var(--label-red)" stroke-width="2"/>
    <line class="frame-rule" x1="-150" y1="124" x2="150" y2="124" stroke="var(--label-red)" stroke-width="2"/>

    <text class="arc-title"><textPath href="#arc-top" startOffset="50%" text-anchor="middle">QUILL BROOK SYRUP</textPath></text>

    <g role="img" aria-label="Irish setter head portrait in front of a red maple leaf">
      <rect x="-80" y="-185" width="150" height="132" rx="26" fill="url(#dog-fill)"/>
    </g>

    <text class="grade" x="-150" y="-71">GRADE A</text>
    <text class="grade" x="145" y="-71" text-anchor="end">AMBER</text>

    <text class="product-main" x="0" y="42" text-anchor="middle">MAPLE</text>

    <g role="img" aria-label="small maple leaf">
      <circle cx="-138" cy="88" r="9" fill="var(--label-red)"/>
    </g>
    <text class="product-sub" x="0" y="108" text-anchor="middle">SYRUP</text>
    <g role="img" aria-label="small maple leaf">
      <circle cx="138" cy="88" r="9" fill="var(--label-red)"/>
    </g>

    <text class="volume" x="0" y="162" text-anchor="middle">8 FL OZ (237ML)</text>

    <text class="arc-place"><textPath href="#arc-bottom" startOffset="50%" text-anchor="middle">BRAMBLE LAKE, VERMONT</textPath></text>
  </svg>
</main>
</body>
</html>
```